Meridale Counsel Corp Business Card design and layout

Meridale Counsel is a small, professional advisory firm specializing in business process consulting and advisory services. We are focused in the energy sector. The business card is to have a combination of blue shades and be professional and serious in nature. Investment banking, capital management, and professional service company card layouts should be used for similar templates

Target Market(s)

Medium to major corporations.

Industry/Entity Type

Consulting

Contact Information for Business Card

The card is to be professional looking in nature and must incorporate the company logo and name in some manner. A two sided design where the opposite side has a QR code and the logo is required.

Logo Text

Brastonhill Partners Inc.

Colors
0592cd
0455a3
3276b5
33a6d7
85cae6
85abd2
cee9f5
cedeed
ecf7fb

Requirements
Must have
• The card is to be professional and have space for employee, title, address, website, and phone numbers (office and cell). The layout must be some shades of blue.
Nice to have
• A space for embossing and/or some subtle gold highlights
Should not have
• Rainbow colours, unprofessional looking fonts (scribble, cursive writing)

```html
<!DOCTYPE html>
<html lang="en">
<head>
<meta charset="utf-8">
<title>Meridale Counsel Corp – Business Card</title>
<link href="https://fonts.googleapis.com/css2?family=Source+Sans+3:wght@400;600&display=swap" rel="stylesheet">
<style>
  :root {
    --navy: #1f3a9a;
    --royal: #0455a3;
    --sky: #33a6d7;
    --ink: #2a3590;
    --muted: #85abd2;
    --tint: #ecf7fb;
    --paper: #ffffff;
    --backdrop: #e9ecef;
    --shadow: rgba(20, 30, 60, 0.18);
  }
  * { margin: 0; padding: 0; box-sizing: border-box; }
  html, body { width: 1200px; height: 1200px; overflow: hidden; }
  body {
    background: var(--backdrop);
    font-family: "Source Sans 3", "Segoe UI", sans-serif;
    display: flex;
    flex-direction: column;
    align-items: center;
    justify-content: center;
    gap: 90px;
  }
  .card {
    position: relative;
    width: 630px;
    height: 360px;
    background: var(--paper);
    box-shadow: 0 14px 40px var(--shadow);
    overflow: hidden;
  }
  .brand { display: flex; align-items: center; gap: 12px; }
  .brand-mark { width: 22px; height: 22px; background: var(--royal); flex: none; }
  .brand-name {
    font-weight: 600;
    font-size: 24px;
    color: var(--royal);
    letter-spacing: 0.5px;
    white-space: nowrap;
  }

  /* Front: contact side */
  .card-front .brand { position: absolute; left: 48px; top: 34px; }
  .person { position: absolute; left: 48px; top: 80px; }
  .person-name { font-size: 27px; color: var(--sky); line-height: 1.1; }
  .person-title { font-size: 16px; color: var(--ink); margin-top: 2px; }
  .contact {
    position: absolute;
    left: 48px;
    top: 146px;
    list-style: none;
    font-size: 14px;
    color: var(--ink);
    line-height: 20px;
  }
  .contact li { display: flex; align-items: center; gap: 9px; white-space: nowrap; }
  .contact svg { width: 12px; height: 12px; fill: var(--ink); flex: none; }
  .contact-label { color: var(--muted); font-weight: 600; width: 40px; }
  .band { position: absolute; left: 0; bottom: 0; width: 100%; height: 84px; }

  /* Back: brand side */
  .card-back {
    display: flex;
    flex-direction: column;
    align-items: center;
    justify-content: center;
    gap: 28px;
  }
  .card-back .brand { gap: 16px; }
  .card-back .brand-name { font-size: 38px; }
  .card-back .brand-mark { width: 32px; height: 32px; }
  .qr-area {
    width: 110px;
    height: 110px;
    background: var(--tint);
    border: 2px solid var(--muted);
  }
</style>
</head>
<body>

  <section class="card card-front" aria-label="Card front">
    <div class="brand">
      <span class="brand-mark"></span>
      <span class="brand-name">Meridale Counsel Corp</span>
    </div>
    <div class="person">
      <p class="person-name">Daniel Marchetti, P.Eng</p>
      <p class="person-title">President</p>
    </div>
    <ul class="contact">
      <li><svg viewBox="0 0 24 24"><path d="M6.6 10.8a15 15 0 0 0 6.6 6.6l2.2-2.2c.3-.3.7-.4 1-.2 1.1.4 2.3.6 3.6.6.6 0 1 .4 1 1V20c0 .6-.4 1-1 1A17 17 0 0 1 3 4c0-.6.4-1 1-1h3.5c.6 0 1 .4 1 1 0 1.3.2 2.5.6 3.6.1.3 0 .7-.2 1z"/></svg><span class="contact-label">Office</span>403-555-0184</li>
      <li><svg viewBox="0 0 24 24"><path d="M7 1h10a2 2 0 0 1 2 2v18a2 2 0 0 1-2 2H7a2 2 0 0 1-2-2V3a2 2 0 0 1 2-2zm0 3v14h10V4z"/></svg><span class="contact-label">Cell</span>403-555-0192</li>
      <li><svg viewBox="0 0 24 24"><path d="M2 5h20v14H2z M2 5l10 8 10-8" fill="none" stroke="#2a3590" stroke-width="2"/></svg>dmarchetti@meridalecounselcorp.com</li>
      <li><svg viewBox="0 0 24 24"><path d="M12 2a10 10 0 1 0 0 20 10 10 0 0 0 0-20zm0 2c1.3 1.6 2.2 3.7 2.4 7H9.6c.2-3.3 1.1-5.4 2.4-7zM4.1 13h3.5c.1 2.5.7 4.6 1.6 6.2A8 8 0 0 1 4.1 13zm0-2a8 8 0 0 1 5.1-6.2C8.3 6.4 7.7 8.5 7.6 11zm5.5 2h4.8c-.2 3.3-1.1 5.4-2.4 7-1.3-1.6-2.2-3.7-2.4-7zm6.8 0h3.5a8 8 0 0 1-5.1 6.2c.9-1.6 1.5-3.7 1.6-6.2zm0-2c-.1-2.5-.7-4.6-1.6-6.2A8 8 0 0 1 19.9 11z"/></svg>www.meridalecounselcorp.com</li>
      <li><svg viewBox="0 0 24 24"><path d="M12 2a7 7 0 0 0-7 7c0 5.2 7 13 7 13s7-7.8 7-13a7 7 0 0 0-7-7zm0 9.5A2.5 2.5 0 1 1 12 6.5a2.5 2.5 0 0 1 0 5z"/></svg>300, 418-9th Ave, SW, Brookfield, AB, T2P 1K4</li>
    </ul>
    <svg class="band" viewBox="0 0 630 84" preserveAspectRatio="none" aria-hidden="true">
      <rect x="0" y="0" width="255" height="84" fill="var(--navy)"/>
      <rect x="270" y="48" width="360" height="36" fill="var(--sky)"/>
    </svg>
  </section>

  <section class="card card-back" aria-label="Card back">
    <div class="brand">
      <span class="brand-mark"></span>
      <span class="brand-name">Meridale Counsel Corp</span>
    </div>
    <div class="qr-area" role="img" aria-label="QR code linking to the company website"></div>
  </section>

</body>
</html>
```